Design a Trade Show Banner

We're a cloud security company launching two new products called Kelvanto Permit and Kelvanto SSH. (Feel free to get some details from our website). Also feel free to leave a wireframe/photo for iPhone and web/monitor screenshots, and I will get updated web/monitor screenshots soon.

We will have a table at BRQN in Austin and need a 2x7 (two foot by seven foot vertical) pop-up banner, like this: http://www.fendralbooth.example/

The logo on our website is not currently in the correct colors.. (please see attached file). We prefer the grey and yellow logo out of the four in the attached Illustrator file (lower-right). (Please don't use the PNG, that's just for looks - if you need other formats for the vector file, let me know.)

Image size should be:
84" (213.36 cm) + 4" (10.16cm) plain white =
88"/223.52cm total length, and
24" (60.96cm) wide.

This is for a tradeshow, so go big and colorful!

Thanks!

```html
<!DOCTYPE html>
<html lang="en">
<head>
<meta charset="utf-8">
<title>Kelvanto – Trade Show Banner</title>
<link rel="stylesheet" href="https://fonts.googleapis.com/css2?family=Archivo+Black&family=Open+Sans:wght@300&display=swap">
<style>
  :root {
    --sky-top: #ffffff;
    --sky-mid: #d4ecfb;
    --sky-low: #7cc4f7;
    --sky-deep: #45a6f1;
    --wordmark-grey: #7b7b7b;
    --accent-yellow: #fbb034;
    --tagline-grey: #4f5356;
    --swoosh-light: rgba(255, 255, 255, 0.85);
    --swoosh-shadow: rgba(70, 80, 90, 0.55);
  }
  html, body {
    margin: 0;
    padding: 0;
    width: 1200px;
    height: 4404px;
    overflow: hidden;
  }
  .banner {
    position: relative;
    width: 1200px;
    height: 4404px;
    overflow: hidden;
    background:
      linear-gradient(100deg, rgba(255,255,255,0) 55%, rgba(255,255,255,0.35) 100%),
      linear-gradient(172deg, var(--sky-top) 0%, var(--sky-top) 14%, var(--sky-mid) 42%, var(--sky-low) 72%, var(--sky-deep) 100%);
  }
  .swooshes {
    position: absolute;
    inset: 0;
    width: 1200px;
    height: 4404px;
  }
  .tagline {
    position: absolute;
    left: 44px;
    top: 310px;
    margin: 0;
    writing-mode: vertical-rl;
    font-family: "Open Sans", sans-serif;
    font-weight: 300;
    font-size: 92px;
    letter-spacing: 6px;
    line-height: 1;
    color: var(--tagline-grey);
    text-transform: uppercase;
    white-space: nowrap;
  }
  .wordmark {
    position: absolute;
    left: 165px;
    top: 250px;
    margin: 0;
    writing-mode: vertical-rl;
    font-family: "Archivo Black", sans-serif;
    font-weight: 400;
    font-size: 420px;
    line-height: 1;
    color: var(--wordmark-grey);
    white-space: nowrap;
  }
  .wordmark-square {
    position: absolute;
    left: 250px;
    top: 2330px;
    width: 120px;
    height: 120px;
    background: var(--accent-yellow);
  }
</style>
</head>
<body>
  <main class="banner">
    <svg class="swooshes" viewBox="0 0 1200 4404" aria-hidden="true">
      <g fill="none" stroke-linecap="round">
        <path d="M1200 880 C 900 1900, 420 3000, 0 3880" stroke="var(--swoosh-shadow)" stroke-width="5"/>
        <path d="M1200 870 C 900 1890, 420 2990, 0 3870" stroke="var(--swoosh-light)" stroke-width="5"/>
        <path d="M1200 1020 C 980 2100, 700 3300, 470 4404" stroke="var(--swoosh-shadow)" stroke-width="4"/>
        <path d="M1200 1010 C 980 2090, 700 3290, 470 4396" stroke="var(--swoosh-light)" stroke-width="4"/>
        <path d="M1200 1650 C 1080 2600, 920 3500, 820 4404" stroke="var(--swoosh-shadow)" stroke-width="3"/>
        <path d="M1200 1640 C 1080 2590, 920 3490, 820 4396" stroke="var(--swoosh-light)" stroke-width="3"/>
      </g>
    </svg>
    <p class="tagline">User management for the cloud</p>
    <h1 class="wordmark">Kelvanto</h1>
    <div class="wordmark-square" aria-hidden="true"></div>
  </main>
</body>
</html>
```